依頼詳細
ゴミ屋敷の片づけ・遺品整理等の事業になります。
ポスティングを想定しています。
ターゲットは高齢者になりますのでわかりやすいデザインでお願いします。
記載項目
屋号:そよかぜクリーンサービス
電話番号:未定
サイズ
A4
ページ数
両面
希望イメージ
シンプル 複雑
単色 カラフル
暗い 明るい
日常 高級
遊び心 厳粛
未来的 伝統的
女性的 男性的
希望する色
緑系
納品ファイル
• 高解像度JPG (.jpg)
補足説明
■ 選んだ理由

高齢者向けということでイラストを多用しわかりやすいデザインで気に入りました。
ベースもやさしめの色合いで好きです。

■ 提案者全員のお礼・コメント

さまざまな提案をいただき感謝しています。ありがとうございました。

```html
<!DOCTYPE html>
<html lang="ja">
<head>
<meta charset="UTF-8">
<title>そよかぜクリーンサービス チラシ</title>
<link href="https://fonts.googleapis.com/css2?family=M+PLUS+Rounded+1c:wght@500;700;800;900&family=Noto+Sans+JP:wght@400;700;900&display=swap" rel="stylesheet">
<style>
:root{
  --green:#4fae3a;
  --green-dark:#2f8a2a;
  --green-pale:#e6f3d4;
  --cream:#fbfaef;
  --blue:#2a7fc4;
  --blue-dark:#14508c;
  --orange:#f08a1c;
  --red:#d8261b;
  --yellow:#fff06a;
  --text:#333;
}
*{margin:0;padding:0;box-sizing:border-box}
html,body{width:846px;height:1200px;overflow:hidden;background:#fff}
body{font-family:"Noto Sans JP",sans-serif;color:var(--text)}
.flyer{position:relative;width:846px;height:1200px;overflow:hidden;background:var(--cream)}
.abs{position:absolute}

/* top bar */
.top-bar{left:0;top:0;width:846px;height:40px;background:var(--green)}
.issue-tag{left:12px;top:6px;padding:2px 12px;background:#fff;color:var(--green-dark);font:900 20px "M PLUS Rounded 1c",sans-serif;border-radius:4px}
.service-list{right:16px;top:8px;color:#fff;font:700 18px "M PLUS Rounded 1c",sans-serif;letter-spacing:.02em}

/* hero */
.hero{left:0;top:40px;width:846px;height:600px;background:linear-gradient(#eaf5dc,#f8fbef 70%,var(--cream))}
.hero-sub{left:0;top:62px;width:846px;text-align:center;font:900 42px "M PLUS Rounded 1c",sans-serif;color:var(--green-dark)}
.hero-sub em{font-style:normal;color:var(--red);font-size:52px}
.hero-title{left:0;top:110px;width:846px;text-align:center;font:900 100px "M PLUS Rounded 1c",sans-serif;color:var(--blue);letter-spacing:.04em;-webkit-text-stroke:3px #fff;paint-order:stroke fill;text-shadow:0 4px 0 var(--blue-dark)}
.art-worker-left{left:20px;top:235px;width:260px;height:300px;border-radius:120px 120px 20px 20px;background:linear-gradient(#bfe0f3,#7fb8dd)}
.art-worker-right{left:566px;top:235px;width:260px;height:300px;border-radius:120px 120px 20px 20px;background:linear-gradient(#bfe0f3,#7fb8dd)}
.art-room{left:292px;top:260px;width:262px;height:270px;border-radius:8px;background:linear-gradient(170deg,#f6f1e6,#e2cfb2)}

/* banner */
.banner{left:40px;top:536px;width:766px;height:108px;background:var(--green);border-radius:12px;border:4px solid #fff;box-shadow:0 3px 0 var(--green-dark)}
.banner-name{left:0;top:6px;width:100%;text-align:center;color:#fff;font:900 42px/1.3 "M PLUS Rounded 1c",sans-serif;letter-spacing:.04em}
.banner-tail{left:0;top:64px;width:100%;text-align:center;color:var(--yellow);font:800 24px/1.2 "M PLUS Rounded 1c",sans-serif}

/* columns */
.section-head{height:44px;border-radius:8px;background:var(--green);color:#fff;font:900 28px "M PLUS Rounded 1c",sans-serif;display:flex;align-items:center;justify-content:center;letter-spacing:.04em}
.sub-head{height:30px;border-radius:6px;background:var(--orange);color:#fff;font:800 19px "M PLUS Rounded 1c",sans-serif;display:flex;align-items:center;padding-left:12px}
.body-text{font-size:15px;line-height:1.6;color:var(--text)}

.tidy-head{left:28px;top:656px;width:390px}
.circle{width:118px;height:118px;border-radius:50%;background:#fff;border:4px solid var(--green);display:flex;align-items:center;justify-content:center;text-align:center;font:800 18px/1.3 "M PLUS Rounded 1c",sans-serif;color:var(--green-dark)}
.circle b{color:var(--red)}
.c1{left:30px;top:708px}.c2{left:165px;top:708px}.c3{left:300px;top:708px}
.electric{left:28px;top:836px;width:390px;height:118px;border:3px solid var(--blue);border-radius:10px;background:#fff;padding:10px 14px}
.electric h3{font:900 19px "M PLUS Rounded 1c",sans-serif;color:var(--blue);margin-bottom:4px}

.estate-head{left:436px;top:656px;width:300px}
.badge-free{left:752px;top:650px;width:72px;height:72px;border-radius:50%;background:var(--red);color:#fff;font:900 15px/1.2 "M PLUS Rounded 1c",sans-serif;display:flex;align-items:center;justify-content:center;text-align:center}
.estate-text{left:436px;top:726px;width:390px}
.trunk-head{left:436px;top:790px;width:390px}
.trunk-text{left:436px;top:822px;width:390px}
.reform-head{left:436px;top:878px;width:390px;background:var(--green)}
.reform-text{left:436px;top:910px;width:390px}

/* purchase */
.purchase{left:28px;top:966px;width:798px;height:82px;background:#fff;border:3px solid var(--red);border-radius:10px}
.purchase-tag{left:0;top:0;width:86px;height:76px;background:var(--red);color:#fff;font:900 26px/1.15 "M PLUS Rounded 1c",sans-serif;display:flex;align-items:center;justify-content:center;text-align:center;border-radius:6px 0 0 6px}
.purchase-title{left:102px;top:6px;font:900 24px "M PLUS Rounded 1c",sans-serif;color:var(--red)}
.purchase-text{left:102px;top:40px;width:680px;font-size:14px;line-height:1.5}

/* footer */
.footer{left:0;top:1056px;width:846px;height:144px;background:var(--green-pale)}
.slogan{left:20px;top:1066px;width:390px;height:46px;background:#fff;border:3px solid var(--green);border-radius:23px;color:var(--green-dark);font:900 21px "M PLUS Rounded 1c",sans-serif;display:flex;align-items:center;justify-content:center}
.slogan-note{left:24px;top:1120px;width:390px;font-size:13px;line-height:1.5}
.cards{left:24px;top:1164px;display:flex;gap:8px}
.cards span{width:44px;height:26px;border-radius:4px;background:#c9d6c0}
.brand-bar{left:430px;top:1066px;width:396px;height:42px;background:var(--green);border-radius:6px;color:#fff;font:900 26px "M PLUS Rounded 1c",sans-serif;display:flex;align-items:center;justify-content:center}
.phone{left:430px;top:1110px;width:396px;display:flex;align-items:center;gap:8px;justify-content:center}
.phone-number{font:900 50px "M PLUS Rounded 1c",sans-serif;color:var(--red);letter-spacing:.01em}
.company{left:430px;top:1172px;width:396px;text-align:center;font-size:12px;color:var(--text)}
</style>
</head>
<body>
<div class="flyer">
  <div class="abs top-bar"></div>
  <div class="abs issue-tag">完全保存版</div>
  <div class="abs service-list">お部屋の片づけ・ゴミ屋敷整理・遺品整理・不用品回収</div>

  <div class="abs hero"></div>
  <div class="abs art-worker-left" role="img" aria-label="青い作業着と帽子の男性スタッフのイラスト"></div>
  <div class="abs art-worker-right" role="img" aria-label="青い作業着と帽子の女性スタッフのイラスト"></div>
  <div class="abs art-room" role="img" aria-label="片付いた明るい部屋と窓のイラスト"></div>
  <div class="abs hero-sub">暮らしの<em>「困った!」</em>に</div>
  <div class="abs hero-title">断捨離請負人</div>

  <div class="abs banner">
    <div class="abs banner-name">そよかぜクリーンサービス</div>
    <div class="abs banner-tail">にお任せください!</div>
  </div>

  <div class="abs section-head tidy-head">暮らしのお片付け</div>
  <div class="abs circle c1"><span>ゴミ屋敷を<br><b>ピカピカに!</b></span></div>
  <div class="abs circle c2"><span>ベランダの<br><b>お掃除!</b></span></div>
  <div class="abs circle c3"><span>不用品の<br><b>処分!</b></span></div>
  <div class="abs electric">
    <h3>電気の「困った」もお任せください!</h3>
    <p class="body-text">エアコンの取付けやウォシュレットの交換など、電気のことならお気軽にご相談ください。</p>
  </div>

  <div class="abs section-head estate-head">遺品の整理</div>
  <div class="abs badge-free">お任せ<br>ください!</div>
  <p class="abs body-text estate-text">思い出が詰まった大切な遺品。当社が丁寧に整理いたします。その他遺品に関するお悩みもご相談ください。</p>
  <div class="abs sub-head trunk-head">トランクルームのお片付け</div>
  <p class="abs body-text trunk-text">お荷物を配置の場所までお運びします。もちろん不用品の処分も可能です!</p>
  <div class="abs sub-head reform-head">リフォーム</div>
  <p class="abs body-text reform-text">高圧洗浄や壁紙の貼り替え、水回りの修理など、住まいのお困りごとにも対応いたします。</p>

  <div class="abs purchase">
    <div class="abs purchase-tag">高価<br>買取</div>
    <div class="abs purchase-title">ただ処分するだけではありません!</div>
    <p class="abs purchase-text">まだ使える家具や家電、骨董品などは高価買取いたします。片付け費用から差し引くことも可能です。</p>
  </div>

  <div class="abs footer"></div>
  <div class="abs slogan">お部屋をキレイに!毎日を快適に!</div>
  <p class="abs slogan-note">お見積もり無料!お電話一本ですぐにお伺いします。各種お支払い方法に対応。</p>
  <div class="abs cards" aria-label="利用できる支払い方法"><span></span><span></span><span></span><span></span><span></span></div>

  <div class="abs brand-bar">そよかぜクリーンサービス</div>
  <div class="abs phone">
    <svg width="46" height="46" viewBox="0 0 24 24" aria-hidden="true"><circle cx="12" cy="12" r="12" fill="#d8261b"/><path d="M8.2 5.5l2 2.6c.3.4.2.9-.1 1.2l-1 1c.7 1.6 2 2.9 3.6 3.6l1-1c.3-.3.8-.4 1.2-.1l2.6 2c.4.3.4.9.1 1.2l-1.2 1.2c-.8.8-2 1-3 .5-3-1.4-5.3-3.7-6.7-6.7-.5-1-.3-2.2.5-3L7 5.4c.3-.3.9-.3 1.2.1z" fill="#fff"/></svg>
    <span class="phone-number">03-0000-1234</span>
  </div>
  <p class="abs company">株式会社そよかぜ企画 〒000-0000 東京都緑野区若葉1-2-3</p>
</div>
</body>
</html>
```